Alapca breeding needs a website

Presentation of the farm, animals (stallions, mares, information about the animals, for sale) and possible later expansion with a webshop (alpaca wool products). We want to present our farm and the animals on the farm on this page. A mission why we are doing this. Furthermore, each animal should be shown with a picture and described. Later we want to sell our own products made from alpaca wool via a webshop. But we still need to grow a bit to do that.

Target Market(s)

Information about my alpaca breeding and the alpaca farm

Industry/Entity Type

Tierzucht

Number of Pages Required

1 page

Font styles to use
Sans Serif

Requirements
Must have
• Modern design that matches the logo
Nice to have
• Intuitive operation / Clear structure
Should not have
• No

```html
<!DOCTYPE html>
<html lang="en">
<head>
<meta charset="utf-8">
<title>Meadowlark Alpacas</title>
<link href="https://fonts.googleapis.com/css2?family=Crimson+Pro:wght@400;500;600;700&display=swap" rel="stylesheet">
<style>
:root{
  --navy:#0e2743;
  --green:#8cc63f;
  --green-soft:#f3fce6;
  --blue:#9fb4cc;
  --grey:#f2f2f2;
  --text:#4a4a4a;
  --muted:#8f8f8f;
  --white:#ffffff;
}
*{margin:0;padding:0;box-sizing:border-box}
html,body{width:1200px;height:4042px;overflow:hidden}
body{position:relative;background:var(--white);font-family:"Crimson Pro",serif;color:var(--text)}
.abs{position:absolute}
a{color:inherit;text-decoration:none}
.topbar{left:0;top:0;width:1200px;height:38px;background:var(--navy);color:var(--white);font-size:11px;display:flex;align-items:center;padding:0 0 0 100px}
.topbar .item{display:flex;align-items:center;gap:8px;padding:0 14px;border-right:1px solid rgba(255,255,255,.6);line-height:14px}
.topbar .item:last-of-type{border-right:0}
.topbar .socials{position:absolute;right:100px;top:12px;display:flex;gap:20px}
.topbar .socials span{width:12px;height:12px;border:1.5px solid var(--white);border-radius:2px;display:block}
.nav a{position:absolute;top:66px;font-size:14px;color:var(--navy)}
.brand{left:540px;top:66px;width:120px;text-align:center;color:var(--navy);font-weight:700;font-size:18px;letter-spacing:1px;line-height:20px}
.brand .mark{display:block;width:34px;height:34px;border-radius:50%;background:var(--navy);margin:0 auto 4px}
.cart-badge{left:1053px;top:62px;width:15px;height:15px;border-radius:50%;background:#e52b2b;color:#fff;font-size:10px;text-align:center;line-height:15px}
.hero-title{left:171px;top:288px;width:520px;font-size:41px;line-height:54px;font-weight:700;color:var(--navy);letter-spacing:.5px}
.hero-text{left:171px;top:476px;width:490px;font-size:13.5px;line-height:20px;color:var(--text)}
.btn{display:flex;align-items:center;justify-content:center;border:2px solid var(--navy);border-radius:22px;color:var(--navy);font-size:13.5px;font-weight:500;background:transparent}
.h2{font-size:43px;line-height:54px;font-weight:700;color:var(--navy);letter-spacing:.5px}
.body{font-size:13.5px;line-height:20px;color:var(--text)}
.more{font-size:13.5px;color:var(--green);text-decoration:underline;display:flex;align-items:center;gap:10px}
.more svg{width:18px;height:10px}
.card{width:246px;height:580px;background:var(--grey);border-radius:16px;overflow:hidden}
.card .photo{width:246px;height:246px;border-radius:50%}
.card h4{margin:24px 18px 0;font-size:14px;font-weight:600;color:#555}
.card p{margin:14px 18px 0;font-size:13.5px;line-height:20px;color:#555}
.card .more{margin:24px 18px 0}
.product{width:246px;background:var(--white);border:1.5px solid var(--green);border-radius:4px}
.product .photo{width:200px;height:220px;margin:26px auto 0;border-radius:6px}
.product h4{margin:22px 14px 0;font-size:24px;line-height:32px;font-weight:600;color:var(--navy)}
.product .row{display:flex;justify-content:space-between;align-items:center;margin:18px 14px 20px}
.product .price{font-size:23px;color:var(--green)}
.product .add{border:1px solid #777;border-radius:14px;font-size:11px;color:#777;padding:5px 20px}
.tile{padding:50px 18px 0}
.tile h3{font-size:42px;line-height:50px;font-weight:700;margin-bottom:20px}
.tile p{font-size:16px;line-height:28.5px}
.footer-col h5{font-size:16px;font-weight:600;color:var(--green);margin-bottom:14px}
.footer-col li{list-style:none;color:var(--white);font-size:11.5px;line-height:28.5px}
.contact li{display:flex;gap:12px;align-items:center;list-style:none;color:var(--white);font-size:11.5px;line-height:34px}
</style>
</head>
<body>

<!-- background bands -->
<svg class="abs" style="left:0;top:0" width="1200" height="4042" aria-hidden="true">
  <path d="M0 190 C150 160 250 175 400 200 C550 225 650 165 800 175 C950 185 1050 200 1200 170 L1200 650 C1050 690 950 640 800 655 C650 670 520 700 380 670 C230 640 120 660 0 690 Z" fill="#f3fce6"/>
  <path d="M0 990 C150 975 250 1005 420 1000 C600 995 700 975 860 990 C1000 1005 1100 985 1200 995 L1200 1410 C1050 1385 950 1400 800 1390 C650 1380 520 1410 380 1395 C230 1380 120 1375 0 1385 Z" fill="#f3fce6"/>
  <path d="M0 2250 C200 2210 350 2235 520 2250 C700 2265 850 2215 1000 2205 C1100 2200 1160 2205 1200 2210 L1200 2890 C1050 2860 900 2870 700 2880 C500 2890 300 2840 0 2850 Z" fill="#f3fce6"/>
  <path d="M0 3725 C200 3700 400 3690 600 3705 C800 3720 1000 3695 1200 3715 L1200 4042 L0 4042 Z" fill="#0e2743"/>
  <path d="M170 3727 C330 3705 480 3700 620 3708 L600 3713 C460 3706 320 3712 170 3727 Z" fill="#8cc63f"/>
  <path d="M700 3722 C860 3706 1000 3706 1110 3712 L1100 3717 C990 3712 860 3712 700 3722 Z" fill="#8cc63f"/>
</svg>

<!-- top bar -->
<div class="abs topbar">
  <div class="item"><svg width="10" height="12" viewBox="0 0 10 12"><path d="M5 0a4 4 0 0 1 4 4c0 3-4 8-4 8S1 7 1 4a4 4 0 0 1 4-4z" fill="#fff"/><circle cx="5" cy="4" r="1.5" fill="#0e2743"/></svg>18 Clover Hill Road, Fernvale 40210</div>
  <div class="item"><svg width="12" height="9" viewBox="0 0 12 9"><rect width="12" height="9" fill="#fff"/><path d="M0 0l6 5 6-5" stroke="#0e2743" fill="none"/></svg>hello@meadowlarkalpacas.com</div>
  <div class="item"><svg width="11" height="11" viewBox="0 0 11 11"><path d="M2 0l2 3-1 1.5c.8 1.5 2 2.7 3.5 3.5L8 7l3 2-1 2C5 11 0 6 0 1z" fill="#fff"/></svg>(555) 014-2290</div>
  <div class="socials"><span></span><span></span><span></span><span></span></div>
</div>

<!-- nav -->
<nav class="nav">
  <a style="left:295px">Home</a>
  <a style="left:364px">About Us</a>
  <a style="left:449px">Products</a>
  <a style="left:716px">Animals</a>
  <a style="left:796px">Contact Us</a>
</nav>
<div class="abs brand"><span class="mark"></span>MEADOWLARK</div>
<svg class="abs" style="left:1038px;top:66px" width="22" height="22" viewBox="0 0 22 22" aria-hidden="true"><path d="M4 7h14l-1.5 12h-11z M8 7V5a3 3 0 0 1 6 0v2" fill="none" stroke="#999" stroke-width="1.5"/></svg>
<div class="abs cart-badge">1</div>
<svg class="abs" style="left:1090px;top:64px" width="24" height="24" viewBox="0 0 24 24" aria-hidden="true"><circle cx="10" cy="10" r="8" fill="none" stroke="#999" stroke-width="1.5"/><path d="M16 16l6 6" stroke="#999" stroke-width="1.5"/></svg>

<!-- hero -->
<h1 class="abs hero-title">LOREM IPSUM DOLOR SIT AMET CONSECTETUR. FAMES ERAT NUNC.</h1>
<p class="abs hero-text">Lorem ipsum dolor sit amet consectetur. Interdum sit pellentesque enim velit. Risus nunc in nisl lobortis aliquet sapien amet eget vitae.</p>
<a class="abs btn" style="left:171px;top:544px;width:158px;height:40px">View All Products</a>
<div class="abs" style="left:730px;top:160px;width:345px;height:462px;border:1.5px solid var(--green);border-radius:175px"></div>
<div class="abs" role="img" aria-label="Portrait of a white llama standing in a grassy field" style="left:748px;top:130px;width:330px;height:494px;border-radius:165px;background:linear-gradient(180deg,#5d6a3c 0%,#9a8f6a 45%,#d9d3c6 70%,#8a7d55 100%)"></div>
<svg class="abs" style="left:1025px;top:640px" width="80" height="16" aria-hidden="true"><circle cx="8" cy="8" r="5" fill="#8cc63f"/><circle cx="29" cy="8" r="5" fill="#d6d6d6"/><circle cx="49" cy="8" r="5" fill="#d6d6d6"/><circle cx="69" cy="8" r="5" fill="#d6d6d6"/></svg>
<div class="abs" role="img" aria-label="Small dark alpaca silhouette decoration" style="left:568px;top:608px;width:62px;height:80px;background:var(--navy);border-radius:30px 30px 8px 8px"></div>

<!-- farm history -->
<h2 class="abs h2" style="left:83px;top:774px;width:460px">Know About Our Farm And History</h2>
<p class="abs body" style="left:609px;top:785px;width:510px">Lorem ipsum dolor sit amet consectetur. Suspendisse est aliquam commodo lectus vivamus gravida quam ipsum a. Neque aenean orci purus justo est lobortis eget ut malesuada. Justo venenatis porttitor eget massa ultrices aliquet a sit id. Neque diam pellentesque mauris massa tempus platea urna etiam massa. Duis ultricies rhoncus adipiscing tellus. Porttitor amet non sed egestas. Vitae id et est sit ut.</p>
<a class="abs more" style="left:609px;top:905px">Learn More <svg viewBox="0 0 18 10"><path d="M0 5h16M12 1l4 4-4 4" stroke="#8cc63f" fill="none"/></svg></a>

<!-- about alpaca -->
<h2 class="abs h2" style="left:83px;top:1066px;width:420px">Know More About Alpaca</h2>
<p class="abs body" style="left:83px;top:1196px;width:500px">Lorem ipsum dolor sit amet consectetur. Suspendisse est aliquam commodo lectus vivamus gravida quam ipsum a. Neque aenean orci purus justo est lobortis eget ut malesuada. Justo venenatis porttitor eget massa ultrices aliquet a sit id. Neque diam pellentesque mauris massa tempus platea urna etiam massa. Duis ultricies rhoncus adipiscing tellus. Porttitor amet non sed egestas. Vitae id et est sit ut.</p>
<a class="abs more" style="left:83px;top:1316px">Learn More <svg viewBox="0 0 18 10"><path d="M0 5h16M12 1l4 4-4 4" stroke="#8cc63f" fill="none"/></svg></a>
<svg class="abs" style="left:600px;top:1000px" width="520" height="400" aria-hidden="true">
  <circle cx="153" cy="170" r="94" fill="#9fb4cc"/>
  <circle cx="348" cy="95" r="94" fill="#c3e39a"/>
  <defs>
    <path id="arcL" d="M38 170 A115 115 0 0 1 153 55"/>
    <path id="arcR" d="M370 -20 A115 115 0 0 1 462 95"/>
  </defs>
  <text font-family="Crimson Pro, serif" font-size="26" font-weight="700" fill="#0e2743" letter-spacing="2"><textPath href="#arcL">I'm Huacaya</textPath></text>
  <text font-family="Crimson Pro, serif" font-size="26" font-weight="700" fill="#0e2743" letter-spacing="2"><textPath href="#arcR">I'm Suri</textPath></text>
</svg>
<div class="abs" role="img" aria-label="White Huacaya alpaca standing" style="left:596px;top:1090px;width:200px;height:290px;border-radius:90px 90px 30px 30px;background:linear-gradient(180deg,#f2efe6,#d9d2c2)"></div>
<div class="abs" role="img" aria-label="Suri alpaca with long silky fleece" style="left:890px;top:1060px;width:225px;height:270px;border-radius:90px 90px 30px 30px;background:linear-gradient(180deg,#e6dfd2,#b8ae9c)"></div>

<!-- animals for sell -->
<h2 class="abs h2" style="left:83px;top:1476px">Animals For Sell</h2>
<a class="abs btn" style="left:959px;top:1484px;width:157px;height:40px">View All</a>

<div class="abs card" style="left:83px;top:1574px">
  <div class="photo" role="img" aria-label="Close-up of a fluffy white alpaca" style="background:linear-gradient(135deg,#e9e7e2,#b9b7b1)"></div>
  <h4>White Alpaca</h4>
  <p>Lorem ipsum dolor sit amet consectetur. Suspendisse est aliquam commodo lectus vivamus gravida quam ipsum a. Neque aenean orci purus justo est lobortis eget ut malesuada. Justo venenatis porttitor eget massa ultrices aliquet a sit id. Neque diam pellentesque mauris massa tempus platea urna etiam massa. Duis ultricies rhoncus adipiscing tellus. Porttitor amet non sed egestas. Vitae id et est sit ut.</p>
  <a class="more">More Details <svg viewBox="0 0 18 10"><path d="M0 5h16M12 1l4 4-4 4" stroke="#8cc63f" fill="none"/></svg></a>
</div>
<div class="abs card" style="left:345px;top:1574px">
  <div class="photo" role="img" aria-label="Baby alpaca in a green pasture" style="background:linear-gradient(160deg,#3f6b2c,#a79a86 55%,#6f3d24)"></div>
  <h4>Baby Alpaca</h4>
  <p>Lorem ipsum dolor sit amet consectetur. Suspendisse est aliquam commodo lectus vivamus gravida quam ipsum a. Neque aenean orci purus justo est lobortis eget ut malesuada. Justo venenatis porttitor eget massa ultrices aliquet a sit id. Neque diam pellentesque mauris massa tempus platea urna etiam massa. Duis ultricies rhoncus adipiscing tellus. Porttitor amet non sed egestas. Vitae id et est sit ut.</p>
  <a class="more">More Details <svg viewBox="0 0 18 10"><path d="M0 5h16M12 1l4 4-4 4" stroke="#8cc63f" fill="none"/></svg></a>
</div>
<div class="abs card" style="left:609px;top:1574px">
  <div class="photo" role="img" aria-label="Brown alpaca in a meadow" style="background:linear-gradient(160deg,#b08457,#c9a27a 45%,#7d8a3a)"></div>
  <h4>Brown Alpaca</h4>
  <p>Lorem ipsum dolor sit amet consectetur. Suspendisse est aliquam commodo lectus vivamus gravida quam ipsum a. Neque aenean orci purus justo est lobortis eget ut malesuada. Justo venenatis porttitor eget massa ultrices aliquet a sit id. Neque diam pellentesque mauris massa tempus platea urna etiam massa. Duis ultricies rhoncus adipiscing tellus. Porttitor amet non sed egestas. Vitae id et est sit ut.</p>
  <a class="more">More Details <svg viewBox="0 0 18 10"><path d="M0 5h16M12 1l4 4-4 4" stroke="#8cc63f" fill="none"/></svg></a>
</div>
<div class="abs card" style="left:871px;top:1574px">
  <div class="photo" role="img" aria-label="Suri stallion alpaca on a hillside" style="background:linear-gradient(180deg,#8a95a6,#a9a08c 50%,#6a6250)"></div>
  <h4>Suri Stallions Alpaca</h4>
  <p>Lorem ipsum dolor sit amet consectetur. Suspendisse est aliquam commodo lectus vivamus gravida quam ipsum a. Neque aenean orci purus justo est lobortis eget ut malesuada. Justo venenatis porttitor eget massa ultrices aliquet a sit id. Neque diam pellentesque mauris massa tempus platea urna etiam massa. Duis ultricies rhoncus adipiscing tellus. Porttitor amet non sed egestas. Vitae id et est sit ut.</p>
  <a class="more">More Details <svg viewBox="0 0 18 10"><path d="M0 5h16M12 1l4 4-4 4" stroke="#8cc63f" fill="none"/></svg></a>
</div>

<!-- products -->
<div class="abs" role="img" aria-label="Brown alpaca head peeking in from the side" style="left:957px;top:2189px;width:243px;height:188px;border-radius:120px 0 0 90px;background:linear-gradient(135deg,#8b6a4c,#b48e6a)"></div>
<h2 class="abs h2" style="left:83px;top:2310px">Alpaca Products</h2>
<a class="abs btn" style="left:784px;top:2324px;width:157px;height:39px">View All Products</a>

<div class="abs product" style="left:83px;top:2391px">
  <div class="photo" role="img" aria-label="Skeins of natural alpaca yarn" style="background:linear-gradient(180deg,#c9bda6,#9d907a)"></div>
  <h4>Alpaca Yarn</h4>
  <div class="row"><span class="price">$35.00</span><span class="add">Add To Cart</span></div>
</div>
<div class="abs product" style="left:345px;top:2391px">
  <div class="photo" role="img" aria-label="Bundle of alpaca roving fibre" style="background:linear-gradient(135deg,#d8d2c6,#a39d92)"></div>
  <h4>Alpaca Roving</h4>
  <div class="row"><span class="price">$28.99</span><span class="add">Add To Cart</span></div>
</div>
<div class="abs product" style="left:609px;top:2391px">
  <div class="photo" role="img" aria-label="Pink ribbed knit beanie" style="background:linear-gradient(180deg,#d86a72,#b9454f)"></div>
  <h4>Pink Ribbed Alpaca Beanie</h4>
  <div class="row"><span class="price">$50.00</span><span class="add">Add To Cart</span></div>
</div>
<div class="abs product" style="left:871px;top:2391px">
  <div class="photo" role="img" aria-label="Olive tweed scarf with fringe" style="background:linear-gradient(180deg,#5f6552,#474b3c)"></div>
  <h4>Alpaca Tweed Scarf</h4>
  <div class="row"><span class="price">$69.99</span><span class="add">Add To Cart</span></div>
</div>

<!-- services grid -->
<div class="abs tile" style="left:83px;top:2939px;width:333px;height:434px;background:var(--blue);color:var(--white)">
  <h3>Our Services</h3>
  <p>Lorem ipsum dolor sit amet consectetur. Diam id a pretium tristique. Imperdiet vivamus ut ipsum viverra vel pulvinar amet et ac. Sit non accumsan dictum tellus dictum quis in nunc sit. Volutpat et quis iaculis dolor sagittis non et eget. Id scelerisque vel cras mauris suspendisse. Eget lacus quam turpis morbi posuere tellus. Praesent cum ut proin orci cursus integer.</p>
</div>
<div class="abs" role="img" aria-label="Alpaca resting on grass by a fence" style="left:83px;top:3392px;width:333px;height:268px;background:linear-gradient(180deg,#6d5a40,#7aa24a 45%,#5d8a34)"></div>
<div class="abs" role="img" aria-label="Alpacas grazing in a fenced pasture" style="left:433px;top:2939px;width:334px;height:266px;background:linear-gradient(180deg,#3f5a2a,#c9b79a 55%,#7d9a4a)"></div>
<div class="abs tile" style="left:433px;top:3224px;width:334px;height:436px;background:var(--green-soft);color:var(--muted)">
  <h3>Our Quality</h3>
  <p>Lorem ipsum dolor sit amet consectetur. Diam id a pretium tristique. Imperdiet vivamus ut ipsum viverra vel pulvinar amet et ac. Sit non accumsan dictum tellus dictum quis in nunc sit. Volutpat et quis iaculis dolor sagittis non et eget. Id scelerisque vel cras mauris suspendisse. Eget lacus quam turpis morbi posuere tellus. Praesent cum ut proin orci cursus integer.</p>
</div>
<div class="abs tile" style="left:783px;top:2939px;width:334px;height:434px;background:var(--grey);color:var(--muted)">
  <h3>Our Animals</h3>
  <p>Lorem ipsum dolor sit amet consectetur. Diam id a pretium tristique. Imperdiet vivamus ut ipsum viverra vel pulvinar amet et ac. Sit non accumsan dictum tellus dictum quis in nunc sit. Volutpat et quis iaculis dolor sagittis non et eget. Id scelerisque vel cras mauris suspendisse. Eget lacus quam turpis morbi posuere tellus. Praesent cum ut proin orci cursus integer.</p>
</div>
<div class="abs" role="img" aria-label="Red barn in front of autumn trees" style="left:783px;top:3392px;width:334px;height:268px;background:linear-gradient(180deg,#d9d8d4 0%,#8a7a3a 35%,#3f5a2a 65%,#587a34 100%)"></div>

<!-- footer -->
<div class="abs" style="left:100px;top:3780px;width:220px;text-align:center;color:var(--white)">
  <div style="font-size:19px;font-weight:700;letter-spacing:1px;display:flex;align-items:center;justify-content:center;gap:8px"><span style="width:26px;height:26px;border-radius:50%;background:var(--white);display:block"></span>MEADOWLARK</div>
  <p style="font-size:11.5px;line-height:20px;margin-top:42px">Lorem ipsum dolor sit amet consectetur. Cras facilisi imperdiet risus tempor volutpat quis.</p>
</div>
<div class="abs footer-col" style="left:433px;top:3780px"><h5>Quick link</h5><ul><li>Homepage</li><li>About Us</li><li>Products</li><li>Animals</li><li>Contact Us</li></ul></div>
<div class="abs footer-col" style="left:576px;top:3780px"><h5>Shopping</h5><ul><li>Alpaca Products</li><li>Cart</li><li>Shipping Information</li><li>Refund and Return Policy</li></ul></div>
<div class="abs footer-col" style="left:764px;top:3780px"><h5>Top Products</h5><ul><li>Alpaca Yarn</li><li>Alpaca Roving</li><li>White Alpaca</li><li>stallions</li><li>mares</li></ul></div>
<div class="abs footer-col" style="left:923px;top:3780px"><h5>Contact Our Farm</h5>
  <ul class="contact">
    <li><svg width="10" height="12" viewBox="0 0 10 12"><path d="M5 0a4 4 0 0 1 4 4c0 3-4 8-4 8S1 7 1 4a4 4 0 0 1 4-4z" fill="#fff"/></svg>18 Clover Hill Road, Fernvale 40210</li>
    <li><svg width="11" height="8" viewBox="0 0 12 9"><rect width="12" height="9" fill="#fff"/><path d="M0 0l6 5 6-5" stroke="#0e2743" fill="none"/></svg>hello@meadowlarkalpacas.com</li>
    <li><svg width="11" height="11" viewBox="0 0 11 11"><path d="M2 0l2 3-1 1.5c.8 1.5 2 2.7 3.5 3.5L8 7l3 2-1 2C5 11 0 6 0 1z" fill="#fff"/></svg>(555) 014-2290</li>
  </ul>
</div>
<div class="abs" style="left:83px;top:3977px;width:1034px;height:1px;background:rgba(255,255,255,.35)"></div>
<p class="abs" style="left:83px;top:3996px;font-size:10.5px;color:var(--white)">2024 © Copyright, Meadowlark Alpacas. All rights reserved.</p>
<div class="abs" style="left:953px;top:3993px;display:flex;gap:26px">
  <span style="width:20px;height:20px;border:2px solid #fff;border-radius:3px;display:block"></span>
  <span style="width:20px;height:20px;border:2px solid #fff;border-radius:3px;display:block"></span>
  <span style="width:20px;height:20px;border:2px solid #fff;border-radius:3px;display:block"></span>
  <span style="width:20px;height:20px;border:2px solid #fff;border-radius:3px;display:block"></span>
</div>

</body>
</html>
```